Home page design for a business selling commercial cleaning machines

We need a home page web design for a wholesale business selling commercial and industrial cleaning machines and spare parts. There is a huge range of products but we don't want the home page to be too cluttered and confusing.
- The design needs to be practical and functional - sharp corners, lots of white with just accents/splashes of the business colours.
- This is a link to their holding page which is very very basic - http://www.vornaspec.co.nz/ - use this to get the accent colours but please use lots and lots more WHITE in the home page design! There are no colour codes available.
- The attached HPID (home page design information) is in table boxes just to see placement of information. Information in orange text. Words to go on the design in black text.
- Expected standard of design examples:
http://brimalo-aquaforce.com/
http://brimalointernational.com/
http://tovesk.com/
http://www.mulfin.wb.gs/ (different industry)
- Only use Google fonts. Non-responsive. Width 1100pixels. Header height (without nav bar) 150-160 pixels.
- Will need a PSD of the chosen homepage design (CS5 compatible)

```html
<!DOCTYPE html>
<html lang="en">
<head>
<meta charset="utf-8">
<title>Vornaspec – Cleaning Machines &amp; Spare Parts</title>
<link href="https://fonts.googleapis.com/css2?family=Roboto:wght@400;500;700&family=Roboto+Condensed:wght@400;700&display=swap" rel="stylesheet">
<style>
:root{
  --orange:#f26b3a;
  --red:#9c1010;
  --red-dark:#5e0606;
  --ink:#222;
  --text:#555;
  --muted:#888;
  --line:#dedede;
  --panel:#e8ecee;
  --soft:#f6f6f6;
  --field:#e9ebec;
  --white:#fff;
}
*{box-sizing:border-box;margin:0;padding:0}
html,body{width:1200px;height:2365px;overflow:hidden;background:var(--white);font-family:"Roboto",sans-serif;color:var(--text)}
.wrap{position:relative;width:820px;margin:0 auto}
/* header */
.site-header{position:relative;height:118px}
.brand{position:absolute;left:0;top:12px;display:flex;align-items:center;gap:6px;font:700 22px "Roboto",sans-serif;color:#333;letter-spacing:-.5px;white-space:nowrap}
.brand-dot{width:10px;height:10px;background:#333}
.header-tag{position:absolute;left:150px;top:8px;font-size:12.5px;line-height:19px;color:#333;white-space:nowrap}
.header-tag .accent{color:var(--orange)}
.header-address{position:absolute;right:0;top:8px;font-size:12px;line-height:17px;color:#333;text-align:right;white-space:nowrap}
.search{position:absolute;left:510px;top:50px;width:160px;height:30px;background:var(--field);font-size:10px;color:var(--muted);padding:9px 8px;white-space:nowrap}
.search-btn{position:absolute;right:0;top:0;width:32px;height:30px;background:var(--orange)}
.search-btn svg{position:absolute;left:9px;top:8px}
.distributors{position:absolute;right:0;top:50px;width:140px;height:30px;border:1.5px solid #333;font-size:12.5px;color:#333;text-align:center;line-height:27px;white-space:nowrap}
.phone{position:absolute;right:0;top:88px;font-size:20px;line-height:24px;color:#222;display:flex;align-items:center;gap:16px;white-space:nowrap}
.header-service{position:absolute;left:0;top:93px;font-size:11.5px;color:#333;white-space:nowrap}
.nav{height:40px;background:linear-gradient(var(--red),var(--red-dark));border-top:2px solid #c31a1a}
.nav ul{list-style:none;display:flex;justify-content:space-between;width:820px;margin:0 auto;height:38px;align-items:center}
.nav li{font:700 12.5px "Roboto Condensed",sans-serif;color:var(--white);text-transform:uppercase;white-space:nowrap;letter-spacing:-.1px}
/* hero */
.hero{position:relative;height:370px;margin-top:4px}
.slider{position:absolute;left:0;top:0;width:535px;height:362px;background:linear-gradient(100deg,#f4f4f4,#e4e4e4);overflow:hidden}
.slide-art{position:absolute;left:190px;top:118px;width:330px;height:215px;background:linear-gradient(150deg,#c9ccce,#8f9599 60%,#b33a2e);border-radius:4px}
.slide-title{position:absolute;left:32px;top:30px;font:700 32px "Roboto",sans-serif;color:var(--orange);line-height:38px}
.slide-sub{position:absolute;left:32px;top:70px;font:500 18px "Roboto",sans-serif;color:#203a5c;white-space:nowrap}
.slide-points{position:absolute;left:32px;top:104px;font-size:18px;line-height:26px;color:#203a5c;white-space:nowrap}
.slide-btn{position:absolute;left:32px;top:190px;width:120px;height:30px;border:1.5px solid #333;background:#fff;font-size:11px;text-align:center;line-height:27px;color:#333}
.dots{position:absolute;left:440px;top:346px;display:flex;gap:4px}
.dots i{width:9px;height:9px;border-radius:50%;border:1px solid #999;background:#fff}
.dots i.on{background:var(--red);border-color:var(--red)}
.why{position:absolute;left:550px;top:14px;width:270px}
.why h2{font:500 24px "Roboto",sans-serif;color:var(--ink);margin-bottom:14px;white-space:nowrap}
.why li{list-style:none;position:relative;padding-left:20px;font-size:12px;line-height:26px;color:#444}
.why li::before{content:"";position:absolute;left:2px;top:8px;width:8px;height:4px;border-left:1.5px solid #6a7f2a;border-bottom:1.5px solid #6a7f2a;transform:rotate(-45deg)}
/* section title */
.section-title{display:flex;align-items:center;gap:20px;font:500 23px "Roboto",sans-serif;color:var(--ink);white-space:nowrap}
.section-title::before,.section-title::after{content:"";flex:1;height:1px;background:var(--line)}
/* range */
.range{margin-top:54px;background:var(--soft);height:370px;border-top:1px solid #eee;border-bottom:1px solid #eee;padding-top:34px}
.range-grid{display:flex;margin-top:20px}
.range-item{width:136.6px;border-right:1px solid #e2e2e2;text-align:center}
.range-item:last-child{border-right:0}
.range-art{height:190px;margin:0 14px;border-radius:3px}
.range-item p{margin-top:14px;font-size:13px;color:#333;white-space:nowrap}
/* feature cards */
.features{display:flex;justify-content:space-between;padding:60px 0 0}
.card{width:258px;height:362px;background:var(--panel);text-align:center;padding:20px 18px 0;position:relative}
.card h3{font:500 13.5px "Roboto",sans-serif;color:#2b3f55;text-transform:uppercase;line-height:19px}
.card-art{height:110px;margin:12px 20px 0;border-radius:3px}
.card p{margin-top:16px;font-size:10.5px;line-height:15px;color:#444}
.btn{display:inline-block;background:var(--orange);color:#fff;font-size:13px;height:32px;line-height:32px;white-space:nowrap}
.card .btn{position:absolute;left:74px;bottom:28px;width:110px}
/* enquiry */
.enquiry{margin-top:56px;border-top:1px solid #eee;padding-top:36px;height:348px}
.enquiry-intro{text-align:center;font-size:11.5px;color:#555;margin-top:6px}
.form{position:relative;height:200px;margin-top:16px}
.field{position:absolute;background:var(--field);font-size:10.5px;color:#444;padding:9px 9px;white-space:nowrap}
.form .btn{position:absolute;left:270px;top:172px;width:263px;height:34px;text-align:center;line-height:34px}
/* brands */
.brands{border-top:1px solid #eee;padding-top:50px;height:226px}
.brand-row{display:flex;align-items:center;justify-content:space-between;margin-top:22px;height:60px}
.brand-name{font:700 17px "Roboto",sans-serif;color:#8a8a8a;width:110px;text-align:center}
.chev{width:16px}
/* footer */
.site-footer{position:relative;background:var(--soft);height:362px;border-top:1px solid #e8e8e8}
.to-top{position:absolute;left:582px;top:-18px;width:36px;height:36px;border-radius:50%;background:var(--orange)}
.to-top svg{position:absolute;left:11px;top:12px}
.footer-cols{position:relative;height:362px}
.col{position:absolute;top:48px;font-size:10.5px;line-height:14.5px;color:#444}
.col h4{font:500 13px "Roboto",sans-serif;color:var(--ink);text-transform:uppercase;margin-bottom:12px;white-space:nowrap}
.col ul{list-style:none}
.col li{white-space:nowrap}
.col .strong{font-weight:700;color:#333}
.post{border-bottom:1px solid #ddd;padding:4px 0 6px;width:210px}
.post small{display:block;color:#777;font-size:10px}
.contact-row{display:flex;gap:8px;margin-bottom:8px;width:180px}
.socials{display:flex;gap:6px;margin-top:8px}
.socials i{width:26px;height:26px;border-radius:50%;background:#b6bcc2}
.socials i:first-child{background:#2f4e8c}
.footer-brand{position:absolute;right:0;bottom:36px;font:700 22px "Roboto",sans-serif;color:#c8c8c8}
</style>
</head>
<body>

<header class="wrap site-header">
  <div class="brand"><span class="brand-dot"></span>VORNASPEC</div>
  <div class="header-tag">Wholesale Importer &amp; Distributor Of Quality<br><span class="accent">Italian Industrial , Commercial &amp; Domestic</span><br>Cleaning Machines &amp; Accessories</div>
  <div class="header-address">4 / 27 Tarren Rd, Ōrewa Flats (office).<br>Open to the public. Head office Marlow Coast</div>
  <div class="search">Search Product<span class="search-btn"><svg width="14" height="14" viewBox="0 0 14 14"><circle cx="6" cy="6" r="4.5" fill="none" stroke="#fff" stroke-width="2"/><path d="M9 9l4 4" stroke="#fff" stroke-width="2"/></svg></span></div>
  <div class="distributors">Distributors NZ wide</div>
  <div class="header-service">Service &amp; supply of most makes and models of cleaning machines and spare parts.</div>
  <div class="phone"><svg width="18" height="14" viewBox="0 0 18 14"><path d="M1 5c0-3 16-3 16 0v2h-5V5H6v2H1z" fill="#999"/><rect x="4" y="8" width="10" height="6" fill="#999"/></svg>04 555 0182</div>
</header>

<nav class="nav">
  <ul>
    <li>Home</li><li>About</li><li>Water Blasters</li><li>Drain Cleaners</li><li>Custom Machines</li><li>Vacuum Cleaners</li><li>Pumps</li><li>Spare Parts</li><li>PTO Machines</li><li>FAQ</li><li>Quote</li><li>Contact</li>
  </ul>
</nav>

<section class="wrap hero">
  <div class="slider">
    <div class="slide-art" role="img" aria-label="Photo of two grey hot high pressure washers on red wheels"></div>
    <div class="slide-title">MASSIMO</div>
    <div class="slide-sub">HOT HIGH PRESSURE WASHER</div>
    <div class="slide-points">Strong<br>Reliable<br>Great for daily use</div>
    <div class="slide-btn">Get More Details</div>
    <div class="dots"><i class="on"></i><i></i><i></i><i></i><i></i><i></i></div>
  </div>
  <div class="why">
    <h2>Why Choose Vornaspec?</h2>
    <ul>
      <li>High quality Italian cleaning machines</li>
      <li>Wide range of brands and models</li>
      <li>Specialist knowledge &amp; expert advice</li>
      <li>Cost of machines – more affordable for top quality</li>
      <li>Able to service and repair all types of cleaning machines</li>
      <li>Huge range of affordable spare parts</li>
      <li>Distributors nationwide offering excellent sales &amp; service support</li>
      <li>Great family business with excellent customer service for over 24 years!</li>
    </ul>
  </div>
</section>

<section class="range">
  <div class="wrap">
    <h2 class="section-title">Huge Range Of Quality Cleaning Machines</h2>
    <div class="range-grid">
      <div class="range-item"><div class="range-art" role="img" aria-label="Photo of an orange upright water blaster" style="background:linear-gradient(#e9e9e9,#e07a2f 60%,#555)"></div><p>Water Blasters</p></div>
      <div class="range-item"><div class="range-art" role="img" aria-label="Photo of a red drain cleaning machine" style="background:linear-gradient(#e9e9e9,#b33 55%,#444)"></div><p>Drain Cleaners</p></div>
      <div class="range-item"><div class="range-art" role="img" aria-label="Photo of a blue floor scrubber machine" style="background:linear-gradient(#e9e9e9,#2c3fb0 55%,#222)"></div><p>Custom Machines</p></div>
      <div class="range-item"><div class="range-art" role="img" aria-label="Photo of a blue canister vacuum cleaner" style="background:linear-gradient(#ececec,#8d9dc0 60%,#3c4b85)"></div><p>Vacuum Cleaners</p></div>
      <div class="range-item"><div class="range-art" role="img" aria-label="Photo of a high pressure pump unit" style="background:linear-gradient(#e9e9e9,#6b5876 55%,#333)"></div><p>Pumps High Pressure</p></div>
      <div class="range-item"><div class="range-art" role="img" aria-label="Photo of a red PTO driven machine" style="background:linear-gradient(#e9e9e9,#d23a28 55%,#333)"></div><p>PTO Machines</p></div>
    </div>
  </div>
</section>

<section class="wrap features">
  <div class="card">
    <h3>Huge Range Of Quality<br>Cleaning Machines</h3>
    <div class="card-art" role="img" aria-label="Photo of a compact blue floor scrubber" style="background:linear-gradient(#e8ecee,#3a5fb8 60%,#222)"></div>
    <p>Browse the products, add any item to a quote request form or give us a call for more information.<br>Not sure what you need? Contact us for expert advice – we're happy to assist!</p>
    <span class="btn">All Products</span>
  </div>
  <div class="card">
    <h3>Nationwide Distributors<br>For Sales &amp; Servicing</h3>
    <div class="card-art" role="img" aria-label="Map of New Zealand with a pin marking the head office" style="background:linear-gradient(135deg,#e8ecee,#1f3f74 55%,#e8ecee)"></div>
    <p>Find out where your local distributor is – Vornaspec has a nationwide network of distributors you can contact direct. Fill in the form below or give us a call to find your local distributor.</p>
    <span class="btn">Contact</span>
  </div>
  <div class="card">
    <h3>Comprehensive Range<br>Of Spare Parts</h3>
    <div class="card-art" role="img" aria-label="Photo of assorted metal machine spare parts" style="background:radial-gradient(circle,#9aa0a6,#e8ecee 70%)"></div>
    <p>Spare parts, servicing &amp; repairs – you want expert knowledge when it comes to any servicing and repairs needed. Vornaspec has a huge range of spare parts and the knowledge to fix virtually any machine.</p>
    <span class="btn">Spare Parts</span>
  </div>
</section>

<section class="enquiry">
  <div class="wrap">
    <h2 class="section-title">Make An Enquiry</h2>
    <p class="enquiry-intro">Would you like a Vornaspec representative to contact you? Please fill in the form and we'll be in touch very soon...</p>
    <div class="form">
      <div class="field" style="left:0;top:0;width:258px;height:32px">First Name</div>
      <div class="field" style="left:280px;top:0;width:258px;height:32px">Last Name</div>
      <div class="field" style="left:562px;top:0;width:258px;height:32px">Contact Phone</div>
      <div class="field" style="left:0;top:52px;width:258px;height:32px">Email Address</div>
      <div class="field" style="left:280px;top:52px;width:540px;height:90px">Any further details?</div>
      <div class="field" style="left:0;top:106px;width:258px;height:32px">Area you live in
        <svg style="position:absolute;right:8px;top:13px" width="9" height="6" viewBox="0 0 9 6"><path d="M0 0h9L4.5 6z" fill="#444"/></svg></div>
      <span class="btn">Send Message</span>
    </div>
  </div>
</section>

<section class="brands">
  <div class="wrap">
    <h2 class="section-title">Our Brands</h2>
    <div class="brand-row">
      <svg class="chev" width="16" height="40" viewBox="0 0 16 40"><path d="M14 2L3 20l11 18" fill="none" stroke="#ccc" stroke-width="2"/></svg>
      <span class="brand-name">FALCOR</span>
      <span class="brand-name">STELLAR</span>
      <span class="brand-name">VELUNOR</span>
      <span class="brand-name">TRIDOS</span>
      <span class="brand-name">AQUARIBE</span>
      <span class="brand-name" style="display:flex;justify-content:center"><span style="width:54px;height:54px;background:#cfcfcf;display:block"></span></span>
      <svg class="chev" width="16" height="40" viewBox="0 0 16 40"><path d="M2 2l11 18L2 38" fill="none" stroke="#ccc" stroke-width="2"/></svg>
    </div>
  </div>
</section>

<footer class="site-footer">
  <span class="to-top"><svg width="14" height="9" viewBox="0 0 14 9"><path d="M1 8l6-6 6 6" fill="none" stroke="#fff" stroke-width="2"/></svg></span>
  <div class="wrap footer-cols">
    <div class="col" style="left:0">
      <h4>Fresh Link</h4>
      <ul><li>Home</li><li>About</li><li>Meet the Team</li><li>Testimonials</li><li>FAQ</li><li>Quote</li><li>Contact/Map</li></ul>
    </div>
    <div class="col" style="left:148px">
      <h4>Products/Services</h4>
      <ul>
        <li class="strong">Water blasters</li><li>- Hot water blasters</li><li>- Cold water blasters electric</li><li>- Cold water blasters petrol or diesel</li><li>- Steam water blasters</li>
        <li class="strong">Drain cleaners</li><li class="strong">Custom machines</li><li class="strong">Vacuum Cleaners</li><li>- Vacuum cleaners</li><li>- Shampoo machines</li>
        <li class="strong">Pumps high pressure</li><li class="strong">Spare Parts</li><li class="strong">PTO machines</li>
      </ul>
    </div>
    <div class="col" style="left:380px">
      <h4>Recent Posts</h4>
      <div class="post">Lorem ipsum dolor sit amet, consectetur<small>22 July 2014</small></div>
      <div class="post">Sed ut perspiciatis unde omnis iste natus<small>21 July 2014</small></div>
      <div class="post" style="border:0">At vero eos et accusamus et iusto<small>20 July 2014</small></div>
    </div>
    <div class="col" style="left:642px">
      <h4>Contact Details</h4>
      <div class="contact-row"><svg width="9" height="12" viewBox="0 0 9 12"><path d="M4.5 0A4.5 4.5 0 0 1 9 4.5C9 8 4.5 12 4.5 12S0 8 0 4.5A4.5 4.5 0 0 1 4.5 0z" fill="#bbb"/></svg><span>Lorem Ipsum is not simply random Harlow College in Brenton 45 BC.</span></div>
      <div class="contact-row"><svg width="10" height="10" viewBox="0 0 10 10"><rect width="10" height="10" fill="#bbb"/></svg><span>+ 04 555 0182</span></div>
      <div class="contact-row"><svg width="10" height="8" viewBox="0 0 10 8"><rect width="10" height="8" fill="#bbb"/></svg><span>accounts@vornaspec.co.nz</span></div>
      <div class="socials"><i></i><i></i><i></i><i></i></div>
    </div>
    <div class="footer-brand">VORNASPEC</div>
  </div>
</footer>

</body>
</html>
```